Flooring Company Wordpress Design Using Elementor

We need a website design using elementor for a flooring company. I have attached a word document with the entire content for the site. I have sample websites www.pellmarbuildersnevada.com and www.tilbrookfinishesreno.com

The site needs to look alot better than the samples. Modern and professional is what we are looking for. 100 times better than the sample websites.

I have images to be used in the site but the file is to large to attached here.

```html
<!DOCTYPE html>
<html lang="en">
<head>
<meta charset="utf-8">
<title>Halcyon Flooring — Premium Flooring Installation in Central Florida</title>
<link href="https://fonts.googleapis.com/css2?family=Manrope:wght@400;600;700;800&family=Heebo:wght@300;400;500;700&display=swap" rel="stylesheet">
<style>
  :root {
    --paper: #fdfcf8;
    --ink: #3a3d52;
    --slate: #4a4e66;
    --slate-deep: #3d3e50;
    --periwinkle: #6576c2;
    --dusk: #6a7395;
    --accent: #f48a3b;
    --muted: #5d6385;
    --body-text: #4b4f63;
    --placeholder: #c3c5d5;
    --line: #e2e3ea;
    --white: #ffffff;
  }
  * { box-sizing: border-box; margin: 0; padding: 0; }
  html, body { width: 1200px; height: 3125px; overflow: hidden; }
  body {
    position: relative;
    background: var(--paper);
    font-family: "Heebo", sans-serif;
    color: var(--body-text);
  }
  .section { position: absolute; left: 0; width: 1200px; }

  /* Navigation */
  .site-nav { top: 0; height: 64px; background: var(--paper); }
  .brand {
    position: absolute; left: 224px; top: 33px;
    font-family: "Manrope", sans-serif; font-weight: 600; font-size: 16px; color: var(--ink);
  }
  .nav-links { position: absolute; right: 226px; top: 38px; display: flex; gap: 20px; list-style: none; }
  .nav-links li { font-size: 10.5px; color: var(--ink); }
  .nav-links .is-current { text-decoration: underline; text-underline-offset: 4px; }

  /* Hero */
  .hero { top: 64px; height: 338px; background: var(--slate); }
  .hero-title {
    position: absolute; left: 224px; top: 72px; width: 380px;
    font-family: "Manrope", sans-serif; font-weight: 700; font-size: 31px; line-height: 33px; color: var(--white);
  }
  .hero-title em { font-style: normal; color: var(--accent); }
  .btn {
    display: flex; align-items: center; justify-content: center;
    font-family: "Heebo", sans-serif; font-weight: 700; font-size: 8.5px; letter-spacing: 0.3px;
    color: var(--white); text-transform: uppercase;
  }
  .btn-solid { position: absolute; background: var(--periwinkle); }
  .btn-ghost { position: absolute; border: 1.2px solid var(--white); }
  .hero .btn-solid { left: 226px; top: 228px; width: 125px; height: 31px; }
  .hero .btn-ghost { left: 357px; top: 228px; width: 125px; height: 31px; }

  /* Features */
  .features { top: 402px; height: 632px; }
  .feature { position: absolute; top: 75px; width: 212px; text-align: center; }
  .feature-icon { width: 86px; height: 88px; margin: 0 auto; background: #e6e7ee; border-radius: 14px; }
  .feature-title {
    margin-top: 42px; font-family: "Heebo", sans-serif; font-weight: 500; font-size: 15.5px; line-height: 19px;
    color: var(--muted); text-transform: uppercase;
  }
  .feature-text { margin-top: 21px; font-size: 10.2px; line-height: 18.8px; font-weight: 300; text-align: justify; color: var(--body-text); }
  .feature-a { left: 226px; } .feature-b { left: 494px; } .feature-c { left: 757px; }
  .warranty-pill {
    position: absolute; left: 413px; top: 520px; width: 373px; height: 36px;
    border: 1.4px solid var(--muted); border-radius: 18px;
    display: flex; align-items: center; justify-content: center;
    font-size: 11px; letter-spacing: 1px; color: var(--muted); text-transform: uppercase;
  }
  .warranty-pill strong { color: var(--accent); font-weight: 700; margin: 0 4px; }

  /* Partner */
  .partner { top: 1034px; height: 400px; background: var(--slate); }
  .partner-panel { position: absolute; left: 0; top: 0; width: 662px; height: 400px; background: var(--slate-deep); }
  .partner-title {
    position: absolute; left: 224px; top: 72px;
    font-family: "Manrope", sans-serif; font-weight: 700; font-size: 25px; color: var(--white);
  }
  .partner-text {
    position: absolute; left: 224px; top: 114px; width: 380px;
    font-size: 10.2px; line-height: 22.5px; color: var(--white);
  }
  .partner .btn-ghost { left: 226px; top: 290px; width: 125px; height: 31px; }

  /* Services */
  .services { top: 1521px; height: 894px; }
  .service-card {
    position: absolute; width: 224px; height: 437px; background: var(--white);
    border-radius: 12px; box-shadow: 0 2px 6px rgba(40, 44, 70, 0.22); overflow: hidden;
  }
  .service-title {
    height: 50px; display: flex; align-items: center; justify-content: center;
    font-weight: 500; font-size: 11.5px; color: var(--muted); text-transform: uppercase;
  }
  .service-image { height: 150px; background: var(--placeholder); }
  .service-text { padding: 20px 18px 0 19px; height: 187px; font-size: 8.6px; line-height: 18.8px; color: var(--muted); }
  .service-actions { display: flex; height: 50px; border-top: 1px solid var(--line); }
  .service-actions span {
    flex: 1; display: flex; align-items: center; justify-content: center;
    font-size: 9px; color: var(--periwinkle);
  }
  .service-actions span + span { border-left: 1px solid var(--line); }
  .col-1 { left: 244px; } .col-2 { left: 488px; } .col-3 { left: 732px; }
  .row-1 { top: 0; } .row-2 { top: 457px; }

  /* Testimonials */
  .testimonials { top: 2490px; height: 381px; background: var(--dusk); }
  .testimonials-title {
    position: absolute; top: 46px; width: 1200px; text-align: center;
    font-family: "Manrope", sans-serif; font-weight: 800; font-size: 22px; letter-spacing: 2px; color: var(--accent);
  }
  .quote-mark {
    position: absolute; left: 377px; top: 100px;
    font-family: "Manrope", sans-serif; font-size: 64px; line-height: 64px; color: transparent;
    -webkit-text-stroke: 1.4px var(--white);
  }
  .quote-text {
    position: absolute; left: 452px; top: 116px; width: 345px;
    font-weight: 300; font-size: 13px; line-height: 22.5px; color: var(--white);
  }
  .quote-author {
    position: absolute; right: 425px; top: 262px;
    font-size: 12.5px; letter-spacing: 1.2px; color: var(--white);
  }
  .testimonials .btn-ghost { left: 536px; top: 301px; width: 125px; height: 31px; }
  .slider-arrow { position: absolute; top: 148px; width: 20px; height: 36px; }
  .slider-prev { left: 224px; } .slider-next { left: 956px; }
</style>
</head>
<body>

<header class="section site-nav">
  <div class="brand">Halcyon Flooring</div>
  <ul class="nav-links">
    <li class="is-current">Home</li>
    <li>About Us</li>
    <li>Service Area</li>
    <li>Our Services</li>
    <li>Testimonial</li>
    <li>Contact Us</li>
  </ul>
</header>

<section class="section hero">
  <h1 class="hero-title">Experience <em>premium</em> flooring installation in Central Florida with Halcyon Group</h1>
  <div class="btn btn-solid">Explore</div>
  <div class="btn btn-ghost">Get a free quote</div>
</section>

<section class="section features">
  <article class="feature feature-a">
    <div class="feature-icon" role="img" aria-label="Line icon of a stressed head with lightning bolts"></div>
    <h2 class="feature-title">Minimal stress<br>on your plate</h2>
    <p class="feature-text">Floor installation or removal can be stressful for both parties. You have to relocate most of your property on the affected area to a new location and adjust your daily operation. The last thing we want to do is add to that. Hence, we take a proactive, customer-focused approach on all our floor installation. We will assist you with your property relocation and covering and ensure a quick and smooth process.</p>
  </article>
  <article class="feature feature-b">
    <div class="feature-icon" role="img" aria-label="Line icon of wooden floor planks"></div>
    <h2 class="feature-title">A floor worthy<br>of your home</h2>
    <p class="feature-text">The quality and type of your floor are as important as its style and appeal. The wrong combination could see you spending a lot on maintenance and feeling frustrated. That's why here at Halcyon Group, don't just go with what is available, but what fits best. We will work with you to identify the kind of floor that matches your lifestyle, theme, preference, and strikes a balance between lower maintenance and durability.</p>
  </article>
  <article class="feature feature-c">
    <div class="feature-icon" role="img" aria-label="Line icon of an award ribbon with a star"></div>
    <h2 class="feature-title">Qualified and<br>certified experts</h2>
    <p class="feature-text">After spending a lot to finally get that property of your dream, the last thing you want is some rookie messing it up and getting you back on your plans. Here at Halcyon Group, we understand this and strive to avoid its occurrence. Hence, we never assign your projects to unvetted professionals. Our team of experts is made up of only highly experienced and passionate individuals licensed in their specific fields to ensure the best results possible.</p>
  </article>
  <div class="warranty-pill">Backed by <strong>1-year</strong> labor warranty</div>
</section>

<section class="section partner">
  <div class="partner-panel"></div>
  <h2 class="partner-title">A reliable partner to lean on.</h2>
  <p class="partner-text">Halcyon Group comes with over 14 years of experience in floor installation. We are specialists when it comes to tile installation, hardwood installation, carpet installation, tile backsplash installation, vinyl installation, laminate floor installation, and floor removal. Over the years, we have come to position ourselves as the professional hands our customers need for all their installation and removal needs. With us, you can be assured of on-time performance, professional services, and prime craftsmanship.</p>
  <div class="btn btn-ghost">Learn more</div>
</section>

<section class="section services">
  <article class="service-card col-1 row-1">
    <h3 class="service-title">Tile installation</h3>
    <div class="service-image" role="img" aria-label="Photo of a tiled floor"></div>
    <p class="service-text">Tile is one durable flooring material that, when placed well, leaves your home or property looking luxurious and inviting. Halcyon Group is fitted with expert tile installers who have experience installing anything tile, from tile flooring, bathroom tile, to backsplash tile. Allow us to make your home or business feel a little more like home.</p>
    <div class="service-actions"><span>Learn More</span><span>Get a Free Quote</span></div>
  </article>
  <article class="service-card col-2 row-1">
    <h3 class="service-title">Hardwood installation</h3>
    <div class="service-image" role="img" aria-label="Photo of a hardwood floor"></div>
    <p class="service-text">Are you looking for the best hardwood installers near you? You are at the right place. Halcyon Group is an expert in all kinds of hardwood installation, from solid to engineered hardwood. We will guide you toward choosing the right wood for your home or business to ensure your space is fixed with the best match.</p>
    <div class="service-actions"><span>Learn More</span><span>Get a Free Quote</span></div>
  </article>
  <article class="service-card col-3 row-1">
    <h3 class="service-title">Laminate installation</h3>
    <div class="service-image" role="img" aria-label="Photo of a laminate floor"></div>
    <p class="service-text">Adorning your floor with laminate material is often a great option to limit scratches, wear and tear, and improve floor durability. With a lot to consider when it comes to picking the right flooring and having it installed, you need an experienced mind by your side. Allow our experts to come to your aid.</p>
    <div class="service-actions"><span>Learn More</span><span>Get a Free Quote</span></div>
  </article>
  <article class="service-card col-1 row-2">
    <h3 class="service-title">Carpet installation</h3>
    <div class="service-image" role="img" aria-label="Photo of a carpeted room"></div>
    <p class="service-text">Carpet installation is a good way to personalized the theme of your home, improve comfort, warmth, and a luxurious feel. With many carpets to choose from down to the tiring installation process, it can be overwhelming. Our team of professional carpet installers are here for you to help you neatly install the carpet that fits your home and floors.</p>
    <div class="service-actions"><span>Learn More</span><span>Get a Free Quote</span></div>
  </article>
  <article class="service-card col-2 row-2">
    <h3 class="service-title">Vinyl installation</h3>
    <div class="service-image" role="img" aria-label="Photo of a vinyl floor"></div>
    <p class="service-text">Vinyl flooring is a great option for families and businesses looking for a balance between the deep texture and feel of real wood, tiles, and stones with the durability, resistance, and low maintenance only dreamed of. Halcyon Group is here to help you through your stages of vinyl floor installation. We will help you get the floor you want in no time at all.</p>
    <div class="service-actions"><span>Learn More</span><span>Get a Free Quote</span></div>
  </article>
  <article class="service-card col-3 row-2">
    <h3 class="service-title">Floor removal</h3>
    <div class="service-image" role="img" aria-label="Photo of an old floor being removed"></div>
    <p class="service-text">Removing your floor isn't an easy task, whether it is a carpet installation, hardwood, or concrete. It takes a lot of time and is filled with risks. Halcyon Group helps you save time and avoid sustaining any injury through the hands of our qualified floor demolition and removal professionals. We will handle both the removal and disposal for you.</p>
    <div class="service-actions"><span>Learn More</span><span>Get a Free Quote</span></div>
  </article>
</section>

<section class="section testimonials">
  <h2 class="testimonials-title">Hear their stories</h2>
  <svg class="slider-arrow slider-prev" viewBox="0 0 20 36" aria-hidden="true"><polyline points="18,2 2,18 18,34" fill="none" stroke="#fff" stroke-width="1.6"/></svg>
  <svg class="slider-arrow slider-next" viewBox="0 0 20 36" aria-hidden="true"><polyline points="2,2 18,18 2,34" fill="none" stroke="#fff" stroke-width="1.6"/></svg>
  <div class="quote-mark" aria-hidden="true">&ldquo;</div>
  <blockquote class="quote-text">We decided to go to with all wood floors in our house. We have used Halcyon Flooring in the past and were impressed with their work. Again, the whole process went smooth and easy. They are very friendly and easy to do business with. The installers were excellent, fast, efficient, and clean. We are very satisfied with the job!</blockquote>
  <p class="quote-author">&ndash; Dana Pruitt</p>
  <div class="btn btn-ghost">Read more</div>
</section>

</body>
</html>
```